Brisk Blends – Eye-Catching Gift Card Design

We are launching a brand-new protein shake, coffee, and supplement shop called Brisk Blends. To celebrate, we want a stunning, unique, and unforgettable gift card design that will stand out in people’s wallets and make them excited to use it.

We will provide:

A gift card template (with exact sizing requirements).

A selection of Brisk Blends logos to work with.

What we’re looking for:

A bold, modern, and creative design that captures our brand’s energy and vibe.

Big, impactful logo placement — don’t be shy, we want our brand to pop.

Incorporation of our tagline:
“Fuel Your Brisk Side.”

A design that is eye-catching, different, and memorable (not generic).

Something that feels premium, fun, and energetic — like our brand.

Style Notes:

Think vibrant, edgy, and powerful, while still being clean and professional.

Open to creative textures, patterns, gradients, or bold color pops.

Should feel like a card people are excited to give and proud to receive.

Deliverables:

Final design in print-ready format following the provided template.

Layered design files (PSD/AI).

About Brisk Blends:

Brisk Blends is more than just a shake bar — we’re the go-to spot for protein drinks, premium supplements, and savage results. Our vibe is high-energy, fitness-driven, and fun.

We can’t wait to see your creativity!

```html
<!DOCTYPE html>
<html lang="en">
<head>
<meta charset="utf-8">
<title>Brisk Blends Gift Card</title>
<link rel="stylesheet" href="https://fonts.googleapis.com/css2?family=Bangers&family=Oswald:wght@500&display=swap">
<style>
  :root {
    --backdrop: #2b2b2b;
    --pink: #ff2fc0;
    --violet: #b46fd0;
    --cyan: #1fe8fb;
    --sky: #5fc8ec;
    --yellow: #fff200;
    --ink: #0d1a2b;
    --white: #ffffff;
    --tile: rgba(255, 255, 255, 0.12);
  }
  html, body {
    margin: 0;
    width: 1200px;
    height: 1200px;
    overflow: hidden;
    background: var(--backdrop);
  }
  .gift-card {
    position: absolute;
    left: 88px;
    top: 273px;
    width: 1025px;
    height: 653px;
    border-radius: 42px;
    overflow: hidden;
    background: linear-gradient(30deg, var(--pink) 0%, var(--violet) 45%, var(--sky) 75%, var(--cyan) 100%);
  }
  .tile {
    position: absolute;
    background: var(--tile);
  }
  .brand-name {
    font-family: "Bangers", cursive;
    color: var(--yellow);
    margin: 0;
    line-height: 1;
    white-space: nowrap;
  }
  .brand-name--hero {
    position: absolute;
    left: 0;
    right: 0;
    top: 290px;
    font-size: 160px;
    letter-spacing: 4px;
    text-align: center;
  }
  .brand-mark--corner {
    position: absolute;
    left: 745px;
    top: 100px;
    display: flex;
    align-items: center;
    gap: 10px;
  }
  .brand-mark--corner .dot {
    width: 20px;
    height: 20px;
    border-radius: 50%;
    background: var(--pink);
    flex: none;
  }
  .brand-mark--corner .brand-name {
    font-size: 36px;
    letter-spacing: 1px;
  }
  .tagline {
    position: absolute;
    left: 0;
    right: 0;
    top: 498px;
    margin: 0;
    text-align: center;
    font-family: "Bangers", cursive;
    font-size: 60px;
    letter-spacing: 2px;
    color: var(--cyan);
    text-shadow: 3px 3px 0 var(--ink), -2px -2px 0 var(--ink), 2px -2px 0 var(--ink), -2px 2px 0 var(--ink);
  }
  .card-field {
    position: absolute;
    top: 590px;
    font-family: "Oswald", sans-serif;
    font-weight: 500;
    font-size: 21px;
    color: var(--white);
    text-transform: uppercase;
  }
  .card-field--number { left: 212px; }
  .card-field--expiry { left: 492px; }
  .expiry-box {
    position: absolute;
    left: 620px;
    top: 582px;
    width: 200px;
    height: 35px;
    background: var(--white);
  }
</style>
</head>
<body>
  <section class="gift-card">
    <div class="tile" style="left:30px;top:0;width:140px;height:125px"></div>
    <div class="tile" style="left:0;top:205px;width:60px;height:240px"></div>
    <div class="tile" style="left:0;top:470px;width:70px;height:90px"></div>
    <div class="tile" style="left:935px;top:10px;width:90px;height:190px"></div>
    <div class="tile" style="left:900px;top:560px;width:70px;height:60px"></div>

    <div class="brand-mark--corner">
      <span class="dot"></span>
      <p class="brand-name">Brisk Blends</p>
    </div>

    <h1 class="brand-name brand-name--hero">Brisk Blends</h1>
    <p class="tagline">Fuel Your Brisk Side</p>

    <span class="card-field card-field--number">Card Number</span>
    <span class="card-field card-field--expiry">Expiry Date</span>
    <div class="expiry-box"></div>
  </section>
</body>
</html>
```